Zielgruppe
Ich bin Schriftsteller und meine Zielgruppe sind hauptsächlich (nicht nur) weibliche Leser.
Hallo liebe Designer,
ich benötige das Cover sowohl als ebook-cover als auch als Cover für ein gedrucktes Taschenbuch.
Folgendes soll auf dem Cover stehen:
Autor: Henrike Grosche
Titel: Die Hütte im Moor
Als kleiner 'Untertitel' soll 'Holding on' stehen und irgendwo unten 'Roman'.
Folgendes ist der Inhalt meines Buches:
An einem heißen Sommertag lernt die schüchterne Svenja den Schriftsteller Jonas Tiedeck kennen. Nach und nach befreit er sie aus ihrem inneren Gefängnis. Ihr Glück scheint perfekt, bis ein Skandal über Jonas hereinbricht, der das Potential hat, nicht nur ihrer beider Liebe, sondern auch ihr Leben zu zerstören.
Schon bald müssen sie erkennen, dass sie es mit einem Feind zu tun haben, dessen Verbindungen nicht nur in höchste Kreise reichen, sondern dessen Köpfe auch nachwachsen, sollte man einen abschlagen.
Eine aufregende Mischung aus Liebesgeschichte, Politthriller und Medienkritik.
Wenn Sie mehr Informationen zum Inhalt bzw. der Stimmung des Romans benötigen, fragen Sie bitte jederzeit.
Für das Cover habe ich folgende Ideen/Vorschläge:
Wenn es mehr in eine realistische Richtung geht, stelle ich mir einen kleinen verwunschen Steg vor. Es soll idyllisch/verwunschen wirken.
Hier ein paar Bilder, die ich schön finde:
https://www.bildquello-archiv.com/de/image-photo/jetty-lake-schmaler-luzin-mecklenburg-vorpommern-5520917364
oder diese Art
https://www.bildquello-archiv.com/de/image-photo/lagow-poland-lake-landscape-7743012659
https://www.bildquello-archiv.com/de/image-photo/wooden-gangplank-into-scenic-lake-6631870245
https://www.bildquello-archiv.com/de/image-photo/ducks-sitting-on-wooden-bridge-pond-8869405132
Wenn Sie Bilder mit einem kleinen Zelt finden, wäre es schön, wenn es auch einen Platz auf dem Cover finden könnte. Das Zelt klein, so das gerade so zwei Personen reinpassen. Es muss auch nicht ganz zu sehen sein, ein Stüc..

```html
<!DOCTYPE html>
<html lang="de">
<head>
<meta charset="utf-8">
<title>Die Hütte im Moor – Buchcover</title>
<link rel="stylesheet" href="https://fonts.googleapis.com/css2?family=Bebas+Neue&family=Open+Sans:wght@400&family=Great+Vibes&family=Libre+Baskerville&display=swap">
<style>
  :root {
    --page-bg: #ffffff;
    --frame-line: #d4d4d4;
    --title-blue: #0b3aa6;
    --sky-top: #3f7fd9;
    --sky-mid: #a7b6ea;
    --sky-low: #e3c6e3;
    --sunset: #f6c9a8;
    --treeline: #3a2a2a;
    --water: #e4b8cf;
    --dock: #4a3328;
  }
  * { margin: 0; padding: 0; box-sizing: border-box; }
  html, body {
    width: 1039px; height: 1200px; overflow: hidden;
    background: var(--page-bg);
  }
  .canvas {
    position: relative; width: 1039px; height: 1200px;
    border: 1px solid var(--frame-line);
  }
  .cover {
    position: absolute; left: 237px; top: 148px;
    width: 566px; height: 905px; overflow: hidden;
  }
  .cover-photo {
    position: absolute; inset: 0;
    background: linear-gradient(180deg,
      var(--sky-top) 0%,
      var(--sky-mid) 22%,
      #c9c7ee 45%,
      var(--sky-low) 58%,
      var(--sunset) 64%,
      var(--treeline) 65.5%,
      var(--treeline) 66.5%,
      var(--water) 68%,
      #c9a6c4 76%,
      #8a5a45 86%,
      var(--dock) 100%);
  }
  .author {
    position: absolute; top: 45px; left: 0; width: 100%;
    text-align: center;
    font-family: "Open Sans", sans-serif; font-size: 25px; line-height: 1.04;
    color: var(--title-blue); letter-spacing: 0.5px;
  }
  .title-word {
    position: absolute;
    font-family: "Bebas Neue", sans-serif; line-height: 1;
    color: var(--title-blue);
  }
  .title-die   { left: 200px; top: 166px; font-size: 67px; }
  .title-huette{ left: 196px; top: 220px; font-size: 121px; }
  .title-im    { left: 150px; top: 322px; font-size: 80px; }
  .title-moor  { left: 215px; top: 313px; font-size: 134px; }
  .subtitle {
    position: absolute; top: 418px; left: 0; width: 100%;
    text-align: center;
    font-family: "Great Vibes", cursive; font-size: 62px; line-height: 1;
    color: var(--title-blue);
  }
  .genre {
    position: absolute; top: 516px; left: 0; width: 100%;
    text-align: center;
    font-family: "Libre Baskerville", serif; font-size: 19px;
    color: var(--title-blue);
  }
</style>
</head>
<body>
  <div class="canvas">
    <div class="cover">
      <div class="cover-photo" role="img" aria-label="Foto: Holzsteg mit Ruderboot und Bank an einem stillen See bei Sonnenuntergang, Schilf im Vordergrund, blauer Himmel mit zarten Wolken"></div>
      <p class="author">HENRIKE<br>GROSCHE</p>
      <span class="title-word title-die">DIE</span>
      <span class="title-word title-huette">HÜTTE</span>
      <span class="title-word title-im">IM</span>
      <span class="title-word title-moor">MOOR</span>
      <p class="subtitle">Holding on</p>
      <p class="genre">ROMAN</p>
    </div>
  </div>
</body>
</html>
```